Website Design for Architecture Practice

I need a home page and one sidebar/content page for an Architecture practice delivered in PSD.

This archictecture practice specialises in one-off, high end homes and commercial properties (restaurant) heavily influenced by Dorian Vessey Kent, particularly his work on the Tarrowby Museum

I am looking for a home page, and a generic content page where we can outline our services, and showcase our homes.

http://notes.qorvenuni.edu.au/studio/Tarrowby%20Lisdane%202.jpg

Target Market(s)

30-70yr old (typically wealthy) property buyers, developers and investors

Industry/Entity Type

Architecture

Number of Pages Required

2 page

Font styles to use
Serif
Sans Serif

Requirements
Must have
• Home page design
• a Content Page design (ie, top nav with sidebar)
Nice to have
• Use any Dorian Vessey Kent images you can find via google etc as placeholders for our own photography (ie they don't need to be licensed as we will be replacing with our own commissioned photography). Full color preferred but feel free to experiment with treating any images as you see fit.

```html
<!DOCTYPE html>
<html lang="en">
<head>
<meta charset="utf-8">
<title>Vessel Nine – Architecture</title>
<link rel="stylesheet" href="https://fonts.googleapis.com/css2?family=Open+Sans:wght@400;600;700&family=Raleway:wght@400;600;700&display=swap">
<style>
:root{
  --orange:#f39a1e;
  --orange-dark:#e0851a;
  --ink:#333333;
  --muted:#777777;
  --line:#e2e2e2;
  --dark:#1f1f1f;
  --darker:#161616;
  --white:#ffffff;
  --sky-top:#9aa4ad;
  --sky-bottom:#5f6a73;
}
*{box-sizing:border-box;margin:0;padding:0}
html,body{width:1200px;height:2356px;overflow:hidden;background:var(--white)}
body{font-family:"Open Sans",Arial,sans-serif;color:var(--ink);position:relative}
.site-header{position:absolute;top:0;left:0;width:1200px;height:64px;display:flex;align-items:center;justify-content:space-between;padding:0 40px 0 40px}
.brand{display:flex;align-items:center;gap:10px}
.brand-dot{width:22px;height:22px;border-radius:50%;background:var(--orange)}
.brand-name{font-family:"Raleway",sans-serif;font-weight:700;font-size:26px;color:var(--orange)}
.main-nav{display:flex;gap:6px}
.main-nav a{font-size:13px;color:var(--ink);text-decoration:none;padding:8px 16px;letter-spacing:.5px}
.main-nav a.active{border:1px solid var(--orange);color:var(--orange)}

.hero{position:absolute;top:64px;left:0;width:1200px;height:590px;background:linear-gradient(180deg,var(--sky-top),#c3c8cc 45%,var(--sky-bottom))}
.hero-caption{position:absolute;left:100px;top:230px;width:430px;background:rgba(20,20,20,.78);padding:22px 24px 22px 24px;color:var(--white)}
.hero-caption h1{font-family:"Raleway",sans-serif;font-size:34px;font-weight:600;letter-spacing:2px}
.hero-caption .bar{width:60px;height:3px;background:var(--orange);margin:12px 0 14px}
.hero-caption p{font-size:13px;line-height:1.6;color:#dddddd}
.slider-arrow{position:absolute;top:300px;width:36px;height:36px;border-radius:50%;background:rgba(255,255,255,.8);display:flex;align-items:center;justify-content:center}
.slider-arrow.prev{left:30px}.slider-arrow.next{right:30px}

.section-title{position:absolute;left:0;width:1200px;text-align:center;font-size:36px;font-weight:400;color:var(--ink)}
.title-rule{position:absolute;left:100px;width:1000px;height:1px;background:var(--line)}
.title-rule span{position:absolute;left:470px;top:-1px;width:60px;height:3px;background:var(--orange)}

.services{position:absolute;top:800px;left:100px;width:1000px;display:flex;justify-content:space-between}
.service{width:300px}
.service .photo{height:172px;background:linear-gradient(160deg,#6a7d90,#b7a58a)}
.service h3{font-size:19px;font-weight:400;margin:28px 0 10px}
.service p{font-size:12px;line-height:1.6;color:var(--muted)}

.welcome{position:absolute;top:1100px;left:0;width:1200px;height:440px;background:linear-gradient(90deg,var(--orange) 0%,var(--orange) 55%,#f5b15a 100%)}
.welcome .portrait{position:absolute;left:190px;top:60px;width:220px;height:380px;background:linear-gradient(180deg,#c9a07a,#2a2d35 60%)}
.welcome .copy{position:absolute;left:580px;top:110px;width:450px;color:var(--white)}
.welcome h2{font-family:"Raleway",sans-serif;font-weight:400;font-size:40px;line-height:1.05}
.welcome h2 strong{display:block;font-size:58px;font-weight:600}
.welcome p{font-size:13px;line-height:1.7;margin:22px 0 22px}
.btn-outline{display:inline-flex;align-items:center;gap:10px;border:1px solid var(--white);color:var(--white);font-size:12px;padding:9px 16px}

.feature-head{position:absolute;top:1590px;left:100px;width:1000px;display:flex;justify-content:space-between;align-items:center}
.feature-head h2{font-size:22px;font-weight:600;letter-spacing:.5px}
.feature-nav{display:flex;gap:8px}
.feature-nav span{width:24px;height:24px;border-radius:50%;background:#e6e6e6;display:flex;align-items:center;justify-content:center}
.works{position:absolute;top:1645px;left:100px;width:1000px;display:flex;justify-content:space-between}
.work{width:236px}
.work .photo{height:185px;background:linear-gradient(170deg,#7c93a9,#d9d3c6)}
.work h4{font-size:13px;font-weight:400;margin:18px 0 8px}
.work p{font-size:11px;line-height:1.6;color:var(--muted)}

.site-footer{position:absolute;top:1975px;left:0;width:1200px;height:280px;background:var(--dark);overflow:hidden}
.footer-accent{position:absolute;left:0;top:0}
.newsletter{position:absolute;left:100px;top:38px;width:260px;color:var(--white)}
.newsletter h5,.contact h5{font-size:13px;font-weight:600;letter-spacing:.5px;margin-bottom:12px}
.newsletter p{font-size:11px;line-height:1.6;color:#aaaaaa;margin-bottom:14px}
.field{height:30px;border:1px solid #555;font-size:11px;color:#999;padding:7px 10px;margin-bottom:10px;width:180px}
.form-row{display:flex;gap:0}
.btn-orange{height:30px;background:var(--orange);color:var(--white);font-size:11px;padding:7px 14px;margin-left:8px}
.contact{position:absolute;left:410px;top:38px;width:220px;color:var(--white)}
.contact p{font-size:11px;line-height:1.7;color:#bbbbbb}
.contact .row{display:flex;align-items:center;gap:10px;font-size:11px;color:#bbbbbb;margin-top:10px}
.testimonial{position:absolute;left:730px;top:20px;width:420px;color:var(--white)}
.testimonial h3{font-size:22px;font-weight:400;margin-bottom:28px}
.testimonial .body{display:flex;gap:24px}
.avatar{width:84px;height:84px;border-radius:50%;background:linear-gradient(160deg,#e3c3a4,#8a6a55);border:3px solid var(--white);flex:none}
.testimonial blockquote{font-size:12px;line-height:1.6}
.testimonial .who{margin-top:14px;font-size:11px}
.testimonial .who b{display:block;font-weight:600}

.bottom-bar{position:absolute;top:2255px;left:0;width:1200px;height:101px;display:flex;align-items:center;justify-content:space-between;padding:0 100px}
.bottom-bar small{font-size:11px;color:var(--muted);letter-spacing:.3px}
.social{display:flex;gap:8px}
.social span{width:26px;height:26px;background:#4a6fa5}
.social span:nth-child(1){background:#d9483b}
.social span:nth-child(2){background:#e4574b}
.social span:nth-child(3){background:#3b5998}
.social span:nth-child(4){background:#1da1f2}
.social span:nth-child(5){background:#0e76a8}
</style>
</head>
<body>

<header class="site-header">
  <div class="brand"><span class="brand-dot"></span><span class="brand-name">Vessel Nine</span></div>
  <nav class="main-nav">
    <a class="active" href="#">HOME</a><a href="#">ABOUT US</a><a href="#">PROPERTIES</a><a href="#">AGENT</a><a href="#">BLOG</a><a href="#">CONTACT US</a>
  </nav>
</header>

<section class="hero" role="img" aria-label="Modern glass office tower with a red sculptural entrance under a grey sky">
  <div class="hero-caption">
    <h1>VESSEL NINE</h1>
    <div class="bar"></div>
    <p>Duis aute irure dolor in reprehenderit in voluptate velit esse cillum dolore eu fugiat nulla pariatur. Excepteur sint.</p>
  </div>
  <span class="slider-arrow prev"><svg width="10" height="14" viewBox="0 0 10 14"><path d="M8 1L2 7l6 6" fill="none" stroke="#333" stroke-width="2"/></svg></span>
  <span class="slider-arrow next"><svg width="10" height="14" viewBox="0 0 10 14"><path d="M2 1l6 6-6 6" fill="none" stroke="#333" stroke-width="2"/></svg></span>
</section>

<h2 class="section-title" style="top:690px">What We Do</h2>
<div class="title-rule" style="top:760px"><span></span></div>

<section class="services">
  <article class="service">
    <div class="photo" role="img" aria-label="High end home with pool at dusk"></div>
    <h3>High end Homes</h3>
    <p>Lorem ipsum dolor sit amet, consectetur adipiscing elit, sed do eiusmod tempor incididunt ut labore et dolore magna aliqua ut enim.</p>
  </article>
  <article class="service">
    <div class="photo" role="img" aria-label="Glass commercial building under blue sky"></div>
    <h3>Commercial Properties</h3>
    <p>Lorem ipsum dolor sit amet, consectetur adipiscing elit, sed do eiusmod tempor incididunt ut labore et dolore magna aliqua ut enim.</p>
  </article>
  <article class="service">
    <div class="photo" role="img" aria-label="Curved metallic museum building by the water"></div>
    <h3>Building Vessel Nine</h3>
    <p>Lorem ipsum dolor sit amet, consectetur adipiscing elit, sed do eiusmod tempor incididunt ut labore et dolore magna aliqua ut enim.</p>
  </article>
</section>

<section class="welcome">
  <div class="portrait" role="img" aria-label="Smiling architect in a dark suit"></div>
  <div class="copy">
    <h2>Welcome To <strong>Vessel Nine</strong></h2>
    <p>Lorem ipsum dolor sit amet, consectetur adipiscing elit, sed do eiusmod tempor incididunt ut labore et dolore magna aliqua. Ut enim ad minim veniam, quis nostrud exercitation ullamco laboris nisi ut aliquip ex ea commodo consequat.</p>
    <span class="btn-outline">Read more <svg width="8" height="10" viewBox="0 0 8 10"><path d="M1 1l5 4-5 4" fill="none" stroke="#fff" stroke-width="1.6"/></svg></span>
  </div>
</section>

<div class="feature-head">
  <h2>FEATURE WORKS</h2>
  <div class="feature-nav">
    <span><svg width="8" height="10" viewBox="0 0 8 10"><path d="M6 1L2 5l4 4" fill="none" stroke="#555" stroke-width="1.6"/></svg></span>
    <span><svg width="8" height="10" viewBox="0 0 8 10"><path d="M2 1l4 4-4 4" fill="none" stroke="#555" stroke-width="1.6"/></svg></span>
  </div>
</div>
<div class="title-rule" style="top:1628px;left:100px"></div>

<section class="works">
  <article class="work"><div class="photo" role="img" aria-label="Skyscraper towers at sunset"></div><h4>Duis aute irure dolor in reprehenderit</h4><p>Lorem ipsum dolor sit amet, consectetur adipiscing elit sed do.</p></article>
  <article class="work"><div class="photo" role="img" aria-label="Modern office block with glass facade"></div><h4>Duis aute irure dolor in reprehenderit</h4><p>Lorem ipsum dolor sit amet, consectetur adipiscing elit sed do.</p></article>
  <article class="work"><div class="photo" role="img" aria-label="White contemporary villa"></div><h4>Duis aute irure dolor in reprehenderit</h4><p>Lorem ipsum dolor sit amet, consectetur adipiscing elit sed do.</p></article>
  <article class="work"><div class="photo" role="img" aria-label="Angular glass building in the city"></div><h4>Duis aute irure dolor in reprehenderit</h4><p>Lorem ipsum dolor sit amet, consectetur adipiscing elit sed do.</p></article>
</section>

<footer class="site-footer">
  <svg class="footer-accent" width="1200" height="280" viewBox="0 0 1200 280"><polygon points="760,0 1200,0 1200,280 680,280" fill="#f39a1e"/></svg>
  <div class="newsletter">
    <h5>SIGN UP FOR NEWSLETTER</h5>
    <p>Excepteur sint occaecat cupidatat non proident, sunt in culpa qui officia.</p>
    <div class="field">Enter Name</div>
    <div class="form-row"><div class="field">Enter Email</div><span class="btn-orange">Subscribe</span></div>
  </div>
  <div class="contact">
    <h5>CONTACT US</h5>
    <p>No. 3, Wren Road,<br>Lincoln LN2 4AB</p>
    <div class="row"><svg width="14" height="14" viewBox="0 0 14 14"><path d="M3 1l2 3-1.5 1.5a8 8 0 0 0 5 5L10 9l3 2-1 2c-6 0-11-5-11-11z" fill="#bbb"/></svg>+44 700 118 2046</div>
    <div class="row"><svg width="14" height="12" viewBox="0 0 14 12"><rect x="1" y="1" width="12" height="10" fill="none" stroke="#bbb"/><path d="M1 1l6 5 6-5" fill="none" stroke="#bbb"/></svg>info@vesselnine.com</div>
  </div>
  <div class="testimonial">
    <h3>What Our Customers Say</h3>
    <div class="body">
      <div class="avatar" role="img" aria-label="Portrait of a client"></div>
      <div>
        <blockquote>“Lorem ipsum dolor sit amet, consectetur adipiscing elit, sed do eiusmod tempor incididunt ut labore et dolore magna aliqua enim.”</blockquote>
        <div class="who"><b>Clara Hewitt</b>Managing Director</div>
      </div>
    </div>
  </div>
</footer>

<div class="bottom-bar">
  <small>COPYRIGHT 2015 VESSEL NINE. ALL RIGHTS RESERVED</small>
  <div class="social"><span></span><span></span><span></span><span></span><span></span></div>
</div>

</body>
</html>
```